Annual Report concept for Government Infrastructure project

Brief:

We are seeking a design concept for our annual report. We would like the front cover, contents pages, as well as 1 double-page spread (so 5 pages all up) within this contest.

This year's report needs to be in B5 size (176 x 250mm / 6.93 x 9.84 inches).

Last year was our first Annual Report and the company was in its early stages. We've progressed a lot and while the old design is quite static, we'd like the new design to have a sense of progress. It should look contemporary and innovative.

Please note that the report is being split into two parts; (1) the layout design (this contest) and (2) the completion of the full report (a follow up project with the winning designer at an agreed budget).

Attached is is last year's version for reference (your can use the content of this within your Cover, Contents, and double-page spread), as well as our branding guidelines.

About our company:

Tarrowdale Freightlink Company Limited (TFC) was established to facilitate the development of an intermodal terminal at Moorebank in Sydney’s south-west.

TFC is a government business enterprise, wholly owned by the Velmoran Crown Authority. TFC aims to optimise private sector expertise and investment, through a competitive process, to develop and operate the intermodal terminal and meet the project’s objectives.

```html
<!DOCTYPE html>
<html lang="en">
<head>
<meta charset="utf-8">
<title>Annual Report 2015 – Contents</title>
<link rel="stylesheet" href="https://fonts.googleapis.com/css2?family=Roboto:ital,wght@0,300;0,400;1,400&family=Arimo:wght@400;700&display=swap">
<style>
  :root {
    --backdrop: #2f5f66;
    --paper: #ffffff;
    --ink: #1c1c1c;
    --rule: #c9c9c9;
    --fold: #dcdcdc;
    --teal: #08979c;
    --tab-side: #9a9a9a;
    --tab-text: #ffffff;
  }
  * { margin: 0; padding: 0; box-sizing: border-box; }
  html, body { width: 1200px; height: 900px; overflow: hidden; }
  body { background: var(--backdrop); font-family: "Arimo", Arial, sans-serif; color: var(--ink); position: relative; }

  .spread { position: absolute; left: 101px; top: 96px; width: 998px; height: 708px; background: var(--paper); }
  .spread__fold { position: absolute; left: 499px; top: 0; width: 1px; height: 100%; background: var(--fold); }

  .running-head { position: absolute; top: 27px; font-size: 8.5px; letter-spacing: 1.8px; }
  .running-head--left { left: 29px; }
  .running-head--right { right: 28px; }
  .head-rule { position: absolute; top: 49px; height: 1px; background: var(--rule); }
  .head-rule--left { left: 29px; width: 427px; }
  .head-rule--right { left: 542px; width: 428px; }

  .page-title { position: absolute; left: 28px; top: 84px; font-family: "Roboto", sans-serif; font-weight: 300; font-size: 26px; letter-spacing: 2.6px; }

  .feature-photo { position: absolute; left: 242px; top: 184px; width: 728px; height: 483px;
    background: linear-gradient(100deg, #8d8a7c 0%, #a49a88 22%, #b07a6a 36%, #b36a5c 55%, #a2564a 75%, #8e4a40 100%); }

  .pull-quote { position: absolute; left: 660px; top: 230px; width: 150px; text-align: center; color: var(--ink); }
  .pull-quote__mark { font-family: "Arimo", Arial, sans-serif; font-weight: 700; font-size: 40px; line-height: 30px; }
  .pull-quote__text { font-family: "Roboto", sans-serif; font-style: italic; font-size: 8.5px; letter-spacing: 1.6px; line-height: 16px; }

  .toc { list-style: none; }
  .toc__item { position: absolute; width: 214px; height: 50px; }
  .toc__label { position: absolute; left: 0; top: 0; width: 200px; height: 41px; background: var(--teal); color: var(--tab-text);
    font-size: 8.8px; letter-spacing: -0.15px; padding: 21px 0 0 8px; white-space: nowrap; }
  .toc__side { position: absolute; left: 200px; top: 0; width: 14px; height: 50px; }

  .folio { position: absolute; bottom: 13px; font-size: 9px; }
  .folio--left { left: 28px; }
  .folio--right { right: 28px; bottom: 18px; }
</style>
</head>
<body>
<main class="spread">
  <div class="spread__fold"></div>

  <p class="running-head running-head--left">ANNUAL REPORT 2015</p>
  <div class="head-rule head-rule--left"></div>
  <p class="running-head running-head--right">ANNUAL REPORT 2015</p>
  <div class="head-rule head-rule--right"></div>

  <h1 class="page-title">CONTENTS</h1>

  <div class="feature-photo" role="img" aria-label="Photograph of a freight train with red shipping containers on the tracks, a rail worker in orange high-visibility clothing climbing onto a wagon beside a green signal ladder"></div>

  <blockquote class="pull-quote">
    <div class="pull-quote__mark">&rdquo;</div>
    <p class="pull-quote__text">THIS IST BLIND COPY<br>AND DITAT<br>CONA REGUSTIS</p>
  </blockquote>

  <ol class="toc">
    <li class="toc__item" style="left:29px;top:282px"><span class="toc__label">04 _ About Tarrowdale Freightlink Company</span><svg class="toc__side" viewBox="0 0 14 50"><polygon points="0,0 14,14 14,50 0,41" fill="var(--tab-side)"/></svg></li>
    <li class="toc__item" style="left:29px;top:338px"><span class="toc__label">06 _ Message from the Chair</span><svg class="toc__side" viewBox="0 0 14 50"><polygon points="0,0 14,14 14,50 0,41" fill="var(--tab-side)"/></svg></li>
    <li class="toc__item" style="left:29px;top:393px"><span class="toc__label">08 _ Message from the CEO</span><svg class="toc__side" viewBox="0 0 14 50"><polygon points="0,0 14,14 14,50 0,41" fill="var(--tab-side)"/></svg></li>
    <li class="toc__item" style="left:29px;top:449px"><span class="toc__label">12 _ Operational Report</span><svg class="toc__side" viewBox="0 0 14 50"><polygon points="0,0 14,14 14,50 0,41" fill="var(--tab-side)"/></svg></li>
    <li class="toc__item" style="left:29px;top:505px"><span class="toc__label">20 _ Directors' Report</span><svg class="toc__side" viewBox="0 0 14 50"><polygon points="0,0 14,14 14,50 0,41" fill="var(--tab-side)"/></svg></li>
    <li class="toc__item" style="left:29px;top:561px"><span class="toc__label">25 _ Auditor's independence declaration</span><svg class="toc__side" viewBox="0 0 14 50"><polygon points="0,0 14,14 14,50 0,41" fill="var(--tab-side)"/></svg></li>
    <li class="toc__item" style="left:29px;top:617px"><span class="toc__label">26 _ Corporate Governance Statement</span><svg class="toc__side" viewBox="0 0 14 50"><polygon points="0,0 14,14 14,50 0,41" fill="var(--tab-side)"/></svg></li>

    <li class="toc__item" style="left:256px;top:338px"><span class="toc__label">30 _ Financial Statements</span><svg class="toc__side" viewBox="0 0 14 50"><polygon points="0,0 14,14 14,50 0,41" fill="var(--tab-side)"/></svg></li>
    <li class="toc__item" style="left:256px;top:393px"><span class="toc__label">34 _ Notes to the Financial Statements</span><svg class="toc__side" viewBox="0 0 14 50"><polygon points="0,0 14,14 14,50 0,41" fill="var(--tab-side)"/></svg></li>
    <li class="toc__item" style="left:256px;top:449px"><span class="toc__label">48 _ Directors' Declaration</span><svg class="toc__side" viewBox="0 0 14 50"><polygon points="0,0 14,14 14,50 0,41" fill="var(--tab-side)"/></svg></li>
    <li class="toc__item" style="left:256px;top:505px"><span class="toc__label">50 _ Independent Auditor's Report</span><svg class="toc__side" viewBox="0 0 14 50"><polygon points="0,0 14,14 14,50 0,41" fill="var(--tab-side)"/></svg></li>
    <li class="toc__item" style="left:256px;top:561px"><span class="toc__label">52 _ Regulatory Reporting Requirements Index</span><svg class="toc__side" viewBox="0 0 14 50"><polygon points="0,0 14,14 14,50 0,41" fill="var(--tab-side)"/></svg></li>
    <li class="toc__item" style="left:256px;top:617px"><span class="toc__label">54 _ Approval by Directors</span><svg class="toc__side" viewBox="0 0 14 50"><polygon points="0,0 14,14 14,50 0,41" fill="var(--tab-side)"/></svg></li>
  </ol>

  <p class="folio folio--left">02</p>
  <p class="folio folio--right">03</p>
</main>
</body>
</html>
```